Acoustic Album Needs Cover Design

Bence Morvath - Intentions: Quiet Harbor

The cover has five parts, each one has obligatory features:

The design in general could be that the person on the pictures is in white, empty space. Solve the shadows as you like, or use no shadows. Up to you.
The album is a happy, minimalistic, zen-like, acoustic album.

I. Main cover

Title: Intentions: Quiet Harbor
Artist: Bence Morvath
Image “01 main cover”

II. Cover inside

Track list (12 songs) with durations
All songs written by Bence Morvath
Copyright Bencetunes 2016.
Image “02 cover inside”

III. Disc

Artist: Bence Morvath
All songs written by Bence Morvath (round on the edge)
Copyright Bencetunes 2016. (round on the edge)
www.bencetunes-example.net (round on the edge)

IV. Under the disc

No words, only some design feature. (Not one of the three images!)

V. Cover back

Track list (same as cover inside)
Copyright Bencetunes 2016.
www.bencetunes-example.net
Image “05 backside”
The paper of this page is longer than the main cover, because it is to be turned up when put in the CD case, and there is the spine with the name of the Artist and Title of the album. On both ends.

Important:
The main cover I need in RGB and also CMYK, all the others only CMYK.
I need the work file (cdr, ai or whatever you use)
I need the CMYK images prepared for printing (sizes set, and that little extra on the edges).
I need the RGB main cover cover in jpeg, 3000x3000 pixels.
That's all. :)

The most important of these all is of course the main cover RGB. Make this one first!

Here’s a sample to listen, it might inspire you:
https://files.filevault-example.net/u/83610457/Quiet%20Harbor%20medley%2020160118.mp3

If you take a closer look at my website, you can see the whole concept.

Good luck and enjoy!
Regards,
Bence

Target Market(s)

New Age spiritual people.

Requirements
Must have
• The three images:
• https://www.filevault-example.net/s/kqpwmrtz7hba2ne/01%20main%20cover%2020160221.jpg?dl=0
• https://www.filevault-example.net/s/9hlyt3wfq5mn8re/02%20cover%20inside%2020160221.jpg?dl=0
• https://www.filevault-example.net/s/pnr4gdk2vjs7bto/05%20backside%2020160221.jpg?dl=0
• If there's a technical problem, let me know!

```html
<!DOCTYPE html>
<html lang="en">
<head>
<meta charset="utf-8">
<title>Bence Morvath – Intentions: Quiet Harbor – Inside Cover and Disc</title>
<link href="https://fonts.googleapis.com/css2?family=Barlow:wght@300&family=Barlow+Condensed:wght@300&display=swap" rel="stylesheet">
<style>
  :root {
    --backdrop: #cdc4a9;
    --paper: #ffffff;
    --photo-light: #f5f5f5;
    --photo-mid: #e8e8ea;
    --ink-grey: #9a9a9a;
    --ink-blue: #5a8fd2;
    --hub-ring: #d4d4d4;
    --hub-inner: #a2a2a2;
  }
  html, body {
    margin: 0;
    width: 1200px;
    height: 900px;
    overflow: hidden;
    background: var(--backdrop);
  }
  .canvas {
    position: relative;
    width: 1200px;
    height: 900px;
  }
  .booklet {
    position: absolute;
    left: 94px;
    top: 226px;
    width: 466px;
    height: 448px;
    background: var(--paper);
  }
  .booklet-photo {
    position: absolute;
    left: 0;
    top: 0;
    width: 258px;
    height: 448px;
    background: linear-gradient(180deg, var(--photo-light) 0%, var(--photo-mid) 100%);
  }
  .tracklist {
    position: absolute;
    top: 63px;
    left: 0;
    margin: 0;
    padding: 0;
    list-style: none;
    font-family: "Barlow Condensed", "Arial Narrow", sans-serif;
    font-weight: 300;
    font-size: 16.5px;
    line-height: 20px;
    color: var(--ink-grey);
    text-transform: uppercase;
  }
  .track {
    display: flex;
    white-space: nowrap;
  }
  .track-title {
    width: 398px;
    text-align: right;
  }
  .track-number {
    margin-left: 24px;
  }
  .credits {
    position: absolute;
    right: 20px;
    top: 384px;
    margin: 0;
    text-align: right;
    white-space: nowrap;
    font-family: "Barlow Condensed", "Arial Narrow", sans-serif;
    font-weight: 300;
    font-size: 13.5px;
    line-height: 15px;
    color: var(--ink-blue);
    text-transform: uppercase;
  }
  .disc {
    position: absolute;
    left: 604px;
    top: 178px;
    width: 540px;
    height: 540px;
  }
  .disc-text {
    font-family: "Barlow", Arial, sans-serif;
    font-weight: 300;
    text-transform: uppercase;
  }
</style>
</head>
<body>
<main class="canvas">
  <section class="booklet" aria-label="Inside cover">
    <div class="booklet-photo" role="img" aria-label="Photo of the barefoot musician standing in white space, resting a hand on an acoustic guitar"></div>
    <ol class="tracklist">
      <li class="track"><span class="track-title">Track something one</span><span class="track-number">01</span></li>
      <li class="track"><span class="track-title">Track something to</span><span class="track-number">02</span></li>
      <li class="track"><span class="track-title">Track something three</span><span class="track-number">03</span></li>
      <li class="track"><span class="track-title">Track something four</span><span class="track-number">04</span></li>
      <li class="track"><span class="track-title">Track something five</span><span class="track-number">05</span></li>
      <li class="track"><span class="track-title">Track something six</span><span class="track-number">06</span></li>
      <li class="track"><span class="track-title">Track something seven</span><span class="track-number">07</span></li>
      <li class="track"><span class="track-title">Track something eight</span><span class="track-number">08</span></li>
      <li class="track"><span class="track-title">Track something nine</span><span class="track-number">09</span></li>
      <li class="track"><span class="track-title">Track something ten</span><span class="track-number">10</span></li>
      <li class="track"><span class="track-title">Track something eleven</span><span class="track-number">11</span></li>
      <li class="track"><span class="track-title">Track something twelve</span><span class="track-number">12</span></li>
    </ol>
    <p class="credits">All songs written by Bence Morvath<br>Copyright Bencetunes 2016.</p>
  </section>

  <svg class="disc" viewBox="0 0 540 540" aria-label="Disc label">
    <defs>
      <path id="edge-ring" d="M270,470 A200,200 0 1 1 270,70 A200,200 0 1 1 270,470"/>
    </defs>
    <circle cx="270" cy="270" r="228" fill="var(--paper)"/>
    <circle cx="270" cy="270" r="72" fill="var(--hub-ring)"/>
    <circle cx="270" cy="270" r="58" fill="var(--hub-inner)"/>
    <circle cx="270" cy="270" r="20" fill="var(--backdrop)"/>

    <text class="disc-text" x="270" y="198" text-anchor="middle" font-size="38" textLength="252" lengthAdjust="spacingAndGlyphs" fill="var(--ink-blue)">Bence Morvath</text>
    <text class="disc-text" x="270" y="366" text-anchor="middle" font-size="24" textLength="296" lengthAdjust="spacingAndGlyphs" fill="var(--ink-grey)">Intentions: Quiet Harbor</text>

    <text class="disc-text" font-size="19" fill="var(--ink-grey)">
      <textPath href="#edge-ring" startOffset="6%" textLength="400" lengthAdjust="spacing">All songs written by Bence Morvath</textPath>
    </text>
    <text class="disc-text" font-size="19" fill="var(--ink-grey)">
      <textPath href="#edge-ring" startOffset="46%" textLength="300" lengthAdjust="spacing">Copyright Bencetunes 2016.</textPath>
    </text>
    <text class="disc-text" font-size="19" fill="var(--ink-grey)">
      <textPath href="#edge-ring" startOffset="73%" textLength="300" lengthAdjust="spacing">www.bencetunes-example.net</textPath>
    </text>
  </svg>
</main>
</body>
</html>
```